OKAV Dispatch (e-update) Design

Using Constant Contact, we need a template news email designed that we can re-use on a regular basis. Our news email would feature an average of 10 content blocks and would love the chance to feature photos with at least 8 of the content blocks. Whatever is designed would need to be transferrable to our constant contact account. Our news content per news item is short, usually a paragraph with links back to our site and events. The template would need a banner that really showcases the email design or helps brand the email. We are looking for a design that is sophisticated but youthful. We recently rebranded our firm and are great with the use of our new corporate colors.

Target Market(s)

Our association members of 700 professional real estate managers of highrises and buildings.

Colors

Designer to choose colors to be used in the design.

Requirements
Must have
• Email template design in Constant Contact to include a banner, area for 8 to 10 content blocks with cooresponding photos. A sophisticated and colorful design that makes people want to read the content.
Should not have
• Clip art

```html
<!DOCTYPE html>
<html lang="en">
<head>
<meta charset="utf-8">
<title>OKAV Dispatch – News Email</title>
<link rel="stylesheet" href="https://fonts.googleapis.com/css2?family=Open+Sans:wght@400;600;700&family=Lato:wght@400;700&display=swap">
<style>
  :root {
    --page-bg: #000000;
    --white: #ffffff;
    --navy: #3d4a7a;
    --indigo: #6473b8;
    --gold: #f5c518;
    --ink: #2a1a1a;
    --body-text: #444444;
    --soft-grey: #efefef;
    --magenta: #a6246a;
    --footer-bg: #4a4a4a;
  }
  * { box-sizing: border-box; margin: 0; padding: 0; }
  html, body { width: 1200px; height: 3396px; overflow: hidden; background: var(--page-bg); }
  body { font-family: "Open Sans", Arial, sans-serif; }

  .email {
    position: absolute; left: 20px; top: 18px; width: 1144px; height: 3355px;
    background: var(--white);
  }

  .masthead {
    height: 159px; display: flex; align-items: center; justify-content: center; gap: 18px;
  }
  .masthead__mark { width: 40px; height: 40px; background: var(--indigo); }
  .masthead__name {
    font-family: "Open Sans", Arial, sans-serif; font-weight: 700; font-size: 52px;
    color: var(--indigo); letter-spacing: 1px;
  }

  .hero {
    position: relative; height: 584px; text-align: center; color: var(--white);
    background: linear-gradient(180deg, #1f2a3a 0%, #33414f 45%, #3a5a32 80%, #2f4a25 100%);
  }
  .hero__photo { position: absolute; inset: 0; }
  .hero__content { position: relative; padding-top: 186px; }
  .hero__title { font-weight: 700; font-size: 58px; letter-spacing: 0.5px; line-height: 1; }
  .hero__text {
    font-family: "Lato", Arial, sans-serif; font-size: 20px; line-height: 29px;
    width: 700px; margin: 24px auto 0;
  }
  .hero__button {
    display: inline-block; margin-top: 24px; width: 142px; height: 48px; line-height: 48px;
    background: var(--gold); color: var(--ink); font-weight: 700; font-size: 16px;
  }

  .intro { text-align: center; padding-top: 34px; }
  .intro__title { color: var(--navy); font-weight: 600; font-size: 38px; }
  .intro__text {
    font-size: 17px; line-height: 28px; color: var(--ink); width: 800px; margin: 16px auto 0;
  }

  .stories {
    display: grid; grid-template-columns: 450px 450px; column-gap: 46px; row-gap: 0;
    margin: 52px 0 0 98px;
  }
  .story { height: 447px; }
  .story__photo { width: 450px; height: 195px; }
  .story__title { font-weight: 700; font-size: 27px; color: var(--ink); margin-top: 22px; }
  .story__text { font-size: 18.5px; line-height: 28px; color: var(--body-text); margin-top: 8px; }
  .story__button {
    display: inline-block; margin-top: 18px; width: 142px; height: 48px; line-height: 48px;
    text-align: center; background: var(--indigo); color: var(--white); font-weight: 700; font-size: 15px;
  }
  .tone-a { background: linear-gradient(180deg, #c9c7c9 0%, #8aa567 55%, #4c7a35 100%); }
  .tone-b { background: linear-gradient(180deg, #8fbde6 0%, #d8d4c6 55%, #6f9a3f 100%); }
  .tone-c { background: linear-gradient(180deg, #5aa7e0 0%, #8e8a86 55%, #b8b4a8 100%); }
  .tone-d { background: linear-gradient(180deg, #7fa6c8 0%, #d2a98a 55%, #7a9a4d 100%); }

  .promo {
    position: absolute; left: 0; top: 2755px; width: 1144px; height: 311px;
    background: var(--soft-grey); text-align: center; padding-top: 70px;
  }
  .promo__title { color: var(--magenta); font-weight: 700; font-size: 44px; line-height: 56px; }
  .promo__text { font-size: 18.5px; line-height: 29px; color: var(--ink); width: 990px; margin: 18px auto 0; }

  .footer {
    position: absolute; left: 0; top: 3066px; width: 1144px; height: 289px;
    background: var(--footer-bg); color: var(--white); text-align: center; padding-top: 52px;
  }
  .footer__social { display: flex; justify-content: center; gap: 22px; }
  .footer__social span { width: 40px; height: 40px; border-radius: 50%; background: var(--white); }
  .footer__text { font-size: 18.5px; line-height: 29px; margin-top: 26px; }
  .footer__links { font-size: 18.5px; margin-top: 26px; }
  .footer__links .sep { margin: 0 8px; }
</style>
</head>
<body>
<main class="email">
  <header class="masthead">
    <span class="masthead__mark"></span>
    <span class="masthead__name">OKAV Dispatch</span>
  </header>

  <section class="hero">
    <div class="hero__photo" role="img" aria-label="Large suburban house with gabled roof and green lawn at dusk"></div>
    <div class="hero__content">
      <h1 class="hero__title">REAL ESTATE MARKET</h1>
      <p class="hero__text">Lorem ipsum dolor sit amet, consec tetuer adipi scing elit, sed diam nonummy nibh euismod tincidunt ut laoreet dolore magna aliquam erat volutpat.</p>
      <span class="hero__button">VIEW MORE</span>
    </div>
  </section>

  <section class="intro">
    <h2 class="intro__title">Paragraph Section Title Here</h2>
    <p class="intro__text">Lorem ipsum dolor sit amet, consectetuer adipiscing elit, sed diam nonummy nibh euismod tincidunt ut laoreet dolore magna aliquam erat volutpat. Ut wisi enim ad minim veniam, quis nostrud.<br>Ut wisi enim ad minim veniam, quis ad nostrud.</p>
  </section>

  <section class="stories">
    <article class="story"><div class="story__photo tone-a" role="img" aria-label="Stone family house with trees"></div><h3 class="story__title">Section Block Title Here</h3><p class="story__text">Lorem ipsum dolor sit amet, consec tetuer adipi elit, sed diam nonummy nibh euismod tincidunt ut laoreet dolore magna aliquam erat volutpat.</p><span class="story__button">VIEW MORE</span></article>
    <article class="story"><div class="story__photo tone-b" role="img" aria-label="White single-storey house with lawn"></div><h3 class="story__title">Section Block Title Here</h3><p class="story__text">Lorem ipsum dolor sit amet, consec tetuer adipi elit, sed diam nonummy nibh euismod tincidunt ut laoreet dolore magna aliquam erat volutpat.</p><span class="story__button">VIEW MORE</span></article>
    <article class="story"><div class="story__photo tone-c" role="img" aria-label="Two-storey stone house under blue sky"></div><h3 class="story__title">Section Block Title Here</h3><p class="story__text">Lorem ipsum dolor sit amet, consec tetuer adipi elit, sed diam nonummy nibh euismod tincidunt ut laoreet dolore magna aliquam erat volutpat.</p><span class="story__button">VIEW MORE</span></article>
    <article class="story"><div class="story__photo tone-d" role="img" aria-label="Brick ranch house with garage"></div><h3 class="story__title">Section Block Title Here</h3><p class="story__text">Lorem ipsum dolor sit amet, consec tetuer adipi elit, sed diam nonummy nibh euismod tincidunt ut laoreet dolore magna aliquam erat volutpat.</p><span class="story__button">VIEW MORE</span></article>
    <article class="story"><div class="story__photo tone-a" role="img" aria-label="Stone family house with trees"></div><h3 class="story__title">Section Block Title Here</h3><p class="story__text">Lorem ipsum dolor sit amet, consec tetuer adipi elit, sed diam nonummy nibh euismod tincidunt ut laoreet dolore magna aliquam erat volutpat.</p><span class="story__button">VIEW MORE</span></article>
    <article class="story"><div class="story__photo tone-b" role="img" aria-label="White single-storey house with lawn"></div><h3 class="story__title">Section Block Title Here</h3><p class="story__text">Lorem ipsum dolor sit amet, consec tetuer adipi elit, sed diam nonummy nibh euismod tincidunt ut laoreet dolore magna aliquam erat volutpat.</p><span class="story__button">VIEW MORE</span></article>
    <article class="story"><div class="story__photo tone-c" role="img" aria-label="Two-storey stone house under blue sky"></div><h3 class="story__title">Section Block Title Here</h3><p class="story__text">Lorem ipsum dolor sit amet, consec tetuer adipi elit, sed diam nonummy nibh euismod tincidunt ut laoreet dolore magna aliquam erat volutpat.</p><span class="story__button">VIEW MORE</span></article>
    <article class="story"><div class="story__photo tone-d" role="img" aria-label="Brick ranch house with garage"></div><h3 class="story__title">Section Block Title Here</h3><p class="story__text">Lorem ipsum dolor sit amet, consec tetuer adipi elit, sed diam nonummy nibh euismod tincidunt ut laoreet dolore magna aliquam erat volutpat.</p><span class="story__button">VIEW MORE</span></article>
  </section>

  <section class="promo">
    <h2 class="promo__title">GOOD PRICE, BETTER LIVING<br>FOR EVERYONE</h2>
    <p class="promo__text">Lorem ipsum dolor sit amet, consectetuer adipiscing elit, sed diam nonummy nibh euismod tincidunt ut laoreet dolore magna aliquam erat volutpat. Ut wisi enim ad minim veniam,quis nostrud. Lorem ipsum dolor sit amet, consectetuer adipiscing elit, sed diam.</p>
  </section>

  <footer class="footer">
    <div class="footer__social" aria-label="Social links">
      <span></span><span></span><span></span><span></span>
    </div>
    <p class="footer__text">Lorem ipsum dolor sit amet, consectetuer adipiscing elit, sed diam nonummy.<br>Lorem ipsum dolor sit amet, consectetuer.</p>
    <p class="footer__links">Unsubscribe<span class="sep">|</span>Manage Subscriptions<span class="sep">|</span>Privacy Policy</p>
  </footer>
</main>
</body>
</html>
```